Vehicle Service Contract Brochure

https://clipvault.example/watch/Tz8mQp2LxRw <- WATCH BEFORE STARTING
Feedback on current designs (generally):
https://clipvault.example/watch/Hn4sKd7WbYe

Finally (from the google doc):UPDATE 10/16/24
The below document is *The Vehicle Service Contract* we need to TURN THIS DOCUMENT into a visual display of customer benefits - use enough panels or pages to display the CUSTOMER BENEFITS in a visually appealing and persuasive way, while displaying the *Vehicle Service Contract* in its entirety, independent of the customer benefits (back pages).

Design a vehicle service contract brochure that car dealerships can present to their customers.

Create a two sided multiple panel brochure:
Audience 1 - Car Buyers
Audience 2 – Car Dealership Sales Person. He / She will use brochure to point out main selling points & differentiators
Audience 3 – Mechanics – they will use this brochure to understand how to file a claim

Main content (customer benefits) for brochure can be found here, Pages 1-9:

https://sheafnotes.example/doc/9Xk2Lm4Pq7Rs1Tv3Wy5Za8Bc6De0Fg/edit?share=on&uid=582093716420957318264&fmt=true&sd=true

Use KT_Example as main guide for content areas / design style.

Use Vexel Shield 1 (page2) as effective example of displaying a high volume of covered items

Our website is qin-vo.com

Please watch before starting:

Need extra days to review

Used Car buyers

Automotive Repair

• QR Codes Pointing to Website
• Icons and infographics
• Too much fine print

```html
<!DOCTYPE html>
<html lang="en">
<head>
<meta charset="utf-8">
<title>Qinvo Dealer Resources – Vehicle Service Contract</title>
<link rel="stylesheet" href="https://fonts.googleapis.com/css2?family=Montserrat:wght@400;500;700&family=Open+Sans:wght@700&display=swap">
<style>
  :root {
    --backdrop: #d7d7d9;
    --paper: #f3f3f3;
    --ink: #1b1b1b;
    --ink-soft: #3c3c3c;
    --brand-red: #e3212b;
    --deep-red: #8e141a;
    --rule-grey: #c9c9c9;
    --band-black: #151515;
    --white: #ffffff;
  }
  * { box-sizing: border-box; margin: 0; padding: 0; }
  html, body { width: 1200px; height: 900px; overflow: hidden; }
  body {
    background: var(--backdrop);
    font-family: "Montserrat", sans-serif;
    color: var(--ink);
    position: relative;
  }
  .brochure-cover {
    position: absolute;
    left: 280px;
    top: 36px;
    width: 640px;
    height: 828px;
    background: var(--paper);
    overflow: hidden;
    box-shadow: 0 10px 30px rgba(0,0,0,0.18);
  }
  .coverage-intro {
    position: absolute;
    left: 300px;
    top: 92px;
    width: 290px;
    font-size: 14px;
    line-height: 1.35;
    color: var(--ink-soft);
  }
  .coverage-intro strong {
    color: var(--brand-red);
    font-weight: 700;
  }
  .intro-rule {
    position: absolute;
    left: 252px;
    top: 196px;
    width: 220px;
    height: 4px;
    background: var(--brand-red);
  }
  .covered-list {
    position: absolute;
    left: 78px;
    top: 228px;
    width: 300px;
    list-style: none;
  }
  .covered-item {
    display: flex;
    align-items: center;
    gap: 8px;
    height: 27px;
    border-bottom: 1px solid var(--rule-grey);
    font-size: 14px;
    font-weight: 500;
    text-transform: uppercase;
    letter-spacing: 0.02em;
    color: var(--ink);
  }
  .tick-icon { width: 13px; height: 13px; flex: none; }
  .brand-name {
    position: absolute;
    left: 78px;
    top: 575px;
    font-size: 24px;
    font-weight: 700;
    color: var(--ink);
    letter-spacing: 0.01em;
  }
  .cover-band {
    position: absolute;
    left: 0;
    bottom: 0;
    width: 640px;
    height: 200px;
  }
  .site-address {
    position: absolute;
    right: 70px;
    bottom: 26px;
    font-family: "Open Sans", sans-serif;
    font-weight: 700;
    font-size: 19px;
    letter-spacing: 0.08em;
    color: var(--white);
  }
</style>
</head>
<body>
  <main class="brochure-cover">
    <p class="coverage-intro">See <strong>“Whats Covered”</strong> sections of steady basics &amp; premier plus plans for reimbursement instructions for plan benefits</p>
    <div class="intro-rule"></div>

    <ul class="covered-list">
      <li class="covered-item"><svg class="tick-icon" viewBox="0 0 14 14"><circle cx="7" cy="7" r="7" fill="#e3212b"/><path d="M3.5 7.2l2.3 2.3 4.7-5" fill="none" stroke="#fff" stroke-width="1.8"/></svg>Engine</li>
      <li class="covered-item"><svg class="tick-icon" viewBox="0 0 14 14"><circle cx="7" cy="7" r="7" fill="#e3212b"/><path d="M3.5 7.2l2.3 2.3 4.7-5" fill="none" stroke="#fff" stroke-width="1.8"/></svg>Transmission</li>
      <li class="covered-item"><svg class="tick-icon" viewBox="0 0 14 14"><circle cx="7" cy="7" r="7" fill="#e3212b"/><path d="M3.5 7.2l2.3 2.3 4.7-5" fill="none" stroke="#fff" stroke-width="1.8"/></svg>Turbos</li>
      <li class="covered-item"><svg class="tick-icon" viewBox="0 0 14 14"><circle cx="7" cy="7" r="7" fill="#e3212b"/><path d="M3.5 7.2l2.3 2.3 4.7-5" fill="none" stroke="#fff" stroke-width="1.8"/></svg>Infotainment</li>
      <li class="covered-item"><svg class="tick-icon" viewBox="0 0 14 14"><circle cx="7" cy="7" r="7" fill="#e3212b"/><path d="M3.5 7.2l2.3 2.3 4.7-5" fill="none" stroke="#fff" stroke-width="1.8"/></svg>Interior Electronics</li>
      <li class="covered-item"><svg class="tick-icon" viewBox="0 0 14 14"><circle cx="7" cy="7" r="7" fill="#e3212b"/><path d="M3.5 7.2l2.3 2.3 4.7-5" fill="none" stroke="#fff" stroke-width="1.8"/></svg>Heating &amp; AC</li>
      <li class="covered-item"><svg class="tick-icon" viewBox="0 0 14 14"><circle cx="7" cy="7" r="7" fill="#e3212b"/><path d="M3.5 7.2l2.3 2.3 4.7-5" fill="none" stroke="#fff" stroke-width="1.8"/></svg>Brake System</li>
      <li class="covered-item"><svg class="tick-icon" viewBox="0 0 14 14"><circle cx="7" cy="7" r="7" fill="#e3212b"/><path d="M3.5 7.2l2.3 2.3 4.7-5" fill="none" stroke="#fff" stroke-width="1.8"/></svg>Steering</li>
      <li class="covered-item"><svg class="tick-icon" viewBox="0 0 14 14"><circle cx="7" cy="7" r="7" fill="#e3212b"/><path d="M3.5 7.2l2.3 2.3 4.7-5" fill="none" stroke="#fff" stroke-width="1.8"/></svg>Suspension</li>
      <li class="covered-item"><svg class="tick-icon" viewBox="0 0 14 14"><circle cx="7" cy="7" r="7" fill="#e3212b"/><path d="M3.5 7.2l2.3 2.3 4.7-5" fill="none" stroke="#fff" stroke-width="1.8"/></svg>Fuel System</li>
      <li class="covered-item"><svg class="tick-icon" viewBox="0 0 14 14"><circle cx="7" cy="7" r="7" fill="#e3212b"/><path d="M3.5 7.2l2.3 2.3 4.7-5" fill="none" stroke="#fff" stroke-width="1.8"/></svg>Seals &amp; Gaskets</li>
    </ul>

    <div class="brand-name">Qinvo Dealer Resources</div>

    <svg class="cover-band" viewBox="0 0 640 200" preserveAspectRatio="none">
      <defs>
        <linearGradient id="photoTone" x1="0" y1="0" x2="1" y2="0">
          <stop offset="0" stop-color="#5a1014"/>
          <stop offset="0.45" stop-color="#a8222a"/>
          <stop offset="1" stop-color="#e3212b"/>
        </linearGradient>
      </defs>
      <g role="img" aria-label="Photo of a red car with its engine bay and components">
        <path d="M0 22 H380 Q392 22 398 14 Q404 6 416 6 H640 V200 H0 Z" fill="url(#photoTone)"/>
      </g>
      <polygon points="520,6 640,6 640,90" fill="#e3212b" opacity="0.85"/>
      <polygon points="0,200 0,170 640,40 640,200" fill="#151515"/>
      <path d="M0 22 H380 Q392 22 398 14 Q404 6 416 6 H640" fill="none" stroke="#151515" stroke-width="5"/>
    </svg>
    <div class="site-address">www.qin-vo.com</div>
  </main>
</body>
</html>
```